Copper Lantern Podcast Business Card Design

Needing a business card with the logo design provided for Copper Lantern Podcast. I am looking for a modern style that fits the current logo.

Info:
Name: Bao Khanh
Title: Creator/Host
Email: bao@copperlanternpod.com
Phone: (405) 637-2918
www.copperlanternpod.com
Twitter: @coplanternpod
Instagram: @copperlanternpodcast
Facebook: Copper Lantern Podcast

Industry/Entity Type

Business

Font styles to use
Sans Serif

Colors
000000
ffffff

Requirements
Must have
• modern, clean design
Nice to have
• social media contact info

```html
<!DOCTYPE html>
<html lang="en">
<head>
<meta charset="utf-8">
<title>Copper Lantern Podcast – Business Card</title>
<link rel="stylesheet" href="https://fonts.googleapis.com/css2?family=Montserrat:wght@700&family=Roboto:wght@400&display=swap">
<style>
  :root {
    --ink: #000000;
    --paper: #ffffff;
    --card-black: #161616;
    --text-dark: #1c1c1c;
    --text-mid: #333333;
    --icon-bg: #d9d9d9;
    --stage: #5e544b;
  }
  html, body {
    margin: 0;
    width: 1200px;
    height: 1200px;
    overflow: hidden;
    background: var(--stage);
  }
  .canvas {
    position: relative;
    width: 1200px;
    height: 1200px;
  }
  .card {
    position: absolute;
    left: 150px;
    width: 900px;
    height: 514px;
    overflow: hidden;
    box-shadow: 0 8px 24px rgba(0,0,0,.35);
  }
  .card--front {
    top: 60px;
    background: var(--card-black);
    display: flex;
    align-items: center;
    justify-content: center;
  }
  .front-wordmark {
    font-family: 'Montserrat', sans-serif;
    font-weight: 700;
    font-size: 44px;
    letter-spacing: 1px;
    color: var(--paper);
    text-transform: uppercase;
  }
  .card--back {
    top: 626px;
    background: linear-gradient(120deg, #ffffff 0%, #f1f1f1 45%, #ffffff 100%);
  }
  .back-wordmark {
    position: absolute;
    left: 60px;
    top: 150px;
    width: 330px;
    display: flex;
    align-items: center;
    gap: 14px;
  }
  .back-wordmark__square {
    width: 44px;
    height: 44px;
    background: var(--ink);
    flex: none;
  }
  .back-wordmark__name {
    font-family: 'Montserrat', sans-serif;
    font-weight: 700;
    font-size: 26px;
    line-height: 1.1;
    color: var(--ink);
    text-transform: uppercase;
  }
  .identity {
    position: absolute;
    left: 460px;
    top: 120px;
  }
  .identity__name {
    font-family: 'Montserrat', sans-serif;
    font-weight: 700;
    font-size: 40px;
    color: var(--ink);
    margin: 0;
    text-transform: uppercase;
  }
  .identity__title {
    font-family: 'Roboto', sans-serif;
    font-size: 24px;
    color: var(--text-mid);
    margin: 2px 0 0;
  }
  .contacts {
    list-style: none;
    margin: 30px 0 0;
    padding: 0;
    font-family: 'Roboto', sans-serif;
    font-size: 22px;
    color: var(--text-dark);
  }
  .contacts li {
    display: flex;
    align-items: center;
    gap: 12px;
    margin-bottom: 10px;
  }
  .contact-icon {
    width: 28px;
    height: 28px;
    flex: none;
  }
  .socials {
    position: absolute;
    left: 60px;
    top: 330px;
    list-style: none;
    margin: 0;
    padding: 0;
    font-family: 'Roboto', sans-serif;
    font-size: 22px;
    color: var(--text-dark);
  }
  .socials li {
    display: flex;
    align-items: center;
    gap: 10px;
    margin-bottom: 6px;
  }
  .socials__marker {
    width: 18px;
    height: 18px;
    background: var(--text-mid);
    flex: none;
  }
  .base-band {
    position: absolute;
    left: 0;
    bottom: 0;
    width: 900px;
    height: 120px;
  }
</style>
</head>
<body>
<main class="canvas">
  <section class="card card--front" aria-label="Card front">
    <div class="front-wordmark">Copper Lantern Podcast</div>
  </section>

  <section class="card card--back" aria-label="Card back">
    <div class="back-wordmark">
      <span class="back-wordmark__square"></span>
      <span class="back-wordmark__name">Copper Lantern Podcast</span>
    </div>

    <div class="identity">
      <h1 class="identity__name">Bao Khanh</h1>
      <p class="identity__title">Creator/ Host</p>
      <ul class="contacts">
        <li>
          <svg class="contact-icon" viewBox="0 0 28 28" aria-hidden="true">
            <rect width="28" height="28" rx="5" fill="var(--icon-bg)"/>
            <path d="M8 9c0 6 5 11 11 11l2-3-3-2-2 1c-2-1-3-2-4-4l1-2-2-3z" fill="var(--text-dark)"/>
          </svg>
          (405) 637-2918
        </li>
        <li>
          <svg class="contact-icon" viewBox="0 0 28 28" aria-hidden="true">
            <rect width="28" height="28" rx="5" fill="var(--icon-bg)"/>
            <g fill="none" stroke="var(--text-dark)" stroke-width="1.5">
              <circle cx="14" cy="14" r="8"/>
              <ellipse cx="14" cy="14" rx="3.5" ry="8"/>
              <line x1="6" y1="14" x2="22" y2="14"/>
            </g>
          </svg>
          www.copperlanternpod.com
        </li>
        <li>
          <svg class="contact-icon" viewBox="0 0 28 28" aria-hidden="true">
            <rect width="28" height="28" rx="5" fill="var(--icon-bg)"/>
            <rect x="6" y="9" width="16" height="11" fill="var(--text-dark)"/>
            <path d="M6 9l8 6 8-6" fill="none" stroke="var(--icon-bg)" stroke-width="1.5"/>
          </svg>
          bao@copperlanternpod.com
        </li>
      </ul>
    </div>

    <ul class="socials">
      <li><span class="socials__marker"></span>@coplanternpod</li>
      <li><span class="socials__marker"></span>Copper Lantern Podcast</li>
      <li><span class="socials__marker"></span>@copperlanternpodcast</li>
    </ul>

    <svg class="base-band" viewBox="0 0 900 120" preserveAspectRatio="none" aria-hidden="true">
      <polygon points="0,96 520,96 540,120 0,120" fill="var(--ink)"/>
      <polygon points="560,70 900,0 900,120 600,120" fill="var(--ink)"/>
    </svg>
  </section>
</main>
</body>
</html>
```